Pro-Athlete Founded Charity Seeks Letterhead Design

A non-profit organization, called Passes for "Discovery: The Dale Wiston Trust," was founded by an PGL athelete to help children born with cardiac heart defects. The charity funds this initiative under the name, "The KINDest Field."

Please create a letterhead considering the following requirements:

- Use Dominant logo: The Kindest Field

- Use Auxillary logo: Passes for Discovery

- Address:4620 North Willow Parkway, Suite 210, Harbor Glen, NV 89017

- Website: www.passesfordiscovery-example.org

- Editable places for date; letter recipients' name/address; signature block

- Coloring: Coastal Herons blue/black (athlete plays for that PGL team); and red (for cardiology/heart disease)... reference logos

Thanks to any and all designers who work on this project! A winner WILL be selected, and follow-on projects will be requested of the winning designer.

```html
<!DOCTYPE html>
<html lang="en">
<head>
<meta charset="utf-8">
<title>Passes for Discovery – Letterhead</title>
<link href="https://fonts.googleapis.com/css2?family=Open+Sans:wght@400;600;700&display=swap" rel="stylesheet">
<style>
  :root {
    --backdrop: #6e6e6e;
    --paper: #ffffff;
    --ink: #1f1f1f;
    --muted: #3a3a3a;
    --heart-red: #e0262f;
    --deep-red: #b5121b;
    --heron-blue: #3cb6e3;
  }
  html, body {
    margin: 0;
    width: 1200px;
    height: 1000px;
    overflow: hidden;
    background: var(--backdrop);
    font-family: "Open Sans", Arial, sans-serif;
  }
  .letterhead {
    position: absolute;
    left: 290px;
    top: 60px;
    width: 620px;
    height: 880px;
    box-sizing: border-box;
    padding: 36px 56px 0 52px;
    background: var(--paper);
    box-shadow: 0 6px 18px rgba(0,0,0,0.35);
    overflow: hidden;
    color: var(--ink);
  }
  .brand-marks {
    display: flex;
    justify-content: flex-end;
    align-items: center;
    gap: 24px;
    height: 92px;
  }
  .brand {
    display: flex;
    align-items: center;
    gap: 8px;
    font-size: 14px;
    font-weight: 700;
    line-height: 1.2;
  }
  .brand--aux { color: var(--heron-blue); }
  .brand--main { color: var(--heart-red); }
  .brand-dot { width: 24px; height: 24px; border-radius: 50%; background: var(--heron-blue); }
  .brand-square { width: 24px; height: 24px; background: var(--heart-red); }

  .address-row {
    display: flex;
    justify-content: space-between;
    align-items: flex-end;
    margin-top: 30px;
    font-size: 11px;
    color: var(--muted);
  }
  .recipient { font-style: normal; line-height: 21px; }
  .recipient .salute { padding-left: 6px; }
  .letter-date { padding-bottom: 0; margin-right: 10px; }

  .letter-body {
    margin-top: 30px;
    font-size: 11px;
    line-height: 21px;
  }
  .letter-body p { margin: 0 0 22px; text-align: justify; }
  .letter-body p.indent { text-indent: 16px; }

  .closing { margin-top: 6px; font-size: 11px; }
  .signature {
    display: block;
    margin: 10px 0 8px;
    width: 150px;
    height: 44px;
    background: linear-gradient(90deg, #f1f1f1, #e4e4e4);
  }

  .contact {
    position: absolute;
    left: 0; right: 0;
    bottom: 60px;
    text-align: center;
    font-size: 9.5px;
    line-height: 16px;
    color: var(--muted);
  }
  .contact .web { color: var(--heart-red); }
  .contact .web::before {
    content: "";
    display: inline-block;
    width: 6px; height: 6px;
    border: 1.5px solid var(--heart-red);
    border-radius: 50%;
    margin-right: 5px;
    vertical-align: -1px;
  }
  .footer-decor {
    position: absolute;
    left: 0; right: 0; bottom: 0;
    height: 52px;
    background: linear-gradient(180deg, var(--heart-red), var(--deep-red));
  }
</style>
</head>
<body>
  <main class="letterhead">
    <header class="brand-marks">
      <div class="brand brand--aux"><span class="brand-dot"></span>Passes for<br>Discovery</div>
      <div class="brand brand--main"><span class="brand-square"></span>The Kindest<br>Field</div>
    </header>

    <div class="address-row">
      <address class="recipient">
        <div class="salute">To</div>
        <div>The Regional Manager,</div>
        <div>Address line Street Name, Area name</div>
        <div>Area code 0000</div>
      </address>
      <div class="letter-date">Date: 00.00.0000</div>
    </div>

    <section class="letter-body">
      <p>specimen book. It has survived not only five centuries, but also the leap into electronic typesetting, remaining essentially unchanged. It was popularised in the 1960s with the release of Letterform sheets containing Lorem Ipsum passages, and more recently with desktop publishing software like Alder PageSetter including versions of Lorem Ipsum.</p>
      <p>opposed to using 'Content here, content here', making it look like readable English. Many desktop publishing packages and web page editors now use Lorem Ipsum as their default model text, and a search for 'lorem ipsum' will uncover many web sites still in their infancy. Various versions have evolved over the years, sometimes by accident, sometimes on purpose (injected humour and the like).</p>
      <p class="indent">Contrary to popular belief, Lorem Ipsum is not simply random text. It has roots in a piece of classical Latin literature from 45 BC, making it over 2000 years old. Robert Hallman, a Latin professor at Hadley-Sutton College in Virginia, looked up one of the more obscure Latin words, consectetur, from a Lorem Ipsum passage, and going through the cites of the word in classical literature, discovered the undoubtable source. Lorem Ipsum comes from sections 1.10.32 and 1.10.33 of "de Finibus Bonorum et Malorum" (The Extremes of Good and Evil) by Aurel Dossani, written in 45 BC. This book</p>
    </section>

    <div class="closing">
      <div>Lorem Ipsum</div>
      <span class="signature" role="img" aria-label="Handwritten signature"></span>
      <div>Lorem Ipsum is a dummy</div>
    </div>

    <div class="contact">
      <div>4620 North Willow Parkway, Suite 210, Harbor Glen, NV 89017</div>
      <div class="web">www.passesfordiscovery-example.org</div>
    </div>
    <div class="footer-decor" role="img" aria-label="Decorative red circle pattern along the bottom edge"></div>
  </main>
</body>
</html>
```